Inspirational Card with Words of Wisdom to Give to Kids

I run basketball camps and give inspirational messages to elementary schools and high schools (www.pastthebrightline.net).

I would like to create a card that has some inspirational thoughts and words of wisdom on it that I can give away...and that students and athletes will keep in their wallet as a reminder of things I've taught them.

I want it to be clean and classy, while not looking too child-like or business-like, as I'd like to be able to give it out to kids, teenagers, and young adults.

The card will be the size of a regular business card and will be double-sided. I would like to use black, orange, gray, and white as the primary colors, with white or gray likely being the background color.
Updates

You're welcome to leave off the title "Wisdom for Life" if desired and just use "The Triple Crown of Success" on the front of the card.

Thanks.

If you choose to leave off the poem, which you're welcome to do, please make one minor addition to the 5-point creed:

Add the words "God and" to "Honour others in everything you say and do" so it becomes:

"Honour God and others in everything you say and do."

Target Market(s)

Children, Teenagers, and Young Adults

Industry/Entity Type

Business

Requirements
Must have
• All the content, although the poem could be removed if necessary.
Should not have
• Nothing basketball-specific, as I want to be able to give it out to any child or teenager.

```html
<!DOCTYPE html>
<html lang="en">
<head>
<meta charset="utf-8">
<title>Wisdom for Life – Wallet Card</title>
<link rel="stylesheet" href="https://fonts.googleapis.com/css2?family=Inconsolata:wght@400;700&display=swap">
<style>
  :root {
    --orange: #f0821e;
    --black: #111111;
    --ink: #1c1c1c;
    --white: #ffffff;
    --gray: #8a8a8a;
    --stage: #2a2a2a;
  }
  * { box-sizing: border-box; margin: 0; padding: 0; }
  html, body { width: 1200px; height: 1200px; overflow: hidden; }
  body {
    background: var(--stage);
    font-family: "Inconsolata", "Consolas", monospace;
    color: var(--ink);
    position: relative;
  }
  .card {
    position: absolute;
    left: 150px;
    width: 900px;
    height: 514px;
    background: var(--white);
    border-radius: 26px;
    overflow: hidden;
  }
  .card--back { top: 58px; }
  .card--front { top: 628px; }
  .card svg.frame { position: absolute; inset: 0; }

  /* back side */
  .creed { position: absolute; left: 48px; top: 70px; width: 470px; }
  .heading { color: var(--orange); font-weight: 700; font-size: 21px; margin-bottom: 14px; }
  .bullets { list-style: none; }
  .bullets li { font-size: 16px; line-height: 1.65; padding-left: 20px; position: relative; }
  .bullets li::before {
    content: ""; position: absolute; left: 2px; top: 9px;
    width: 7px; height: 7px; background: var(--orange); border-radius: 50%;
  }
  .pledge { position: absolute; left: 545px; top: 70px; width: 320px; }
  .pledge p { font-size: 15px; line-height: 1.5; margin-top: 10px; }
  .sign-line { margin-top: 34px; margin-left: 110px; width: 190px; border-top: 1.5px solid var(--ink); font-size: 10px; text-align: center; padding-top: 3px; }
  .sign-line + .sign-line { margin-top: 24px; }
  .live-title { position: absolute; left: 0; right: 0; top: 368px; text-align: center; font-weight: 700; font-size: 22px; }
  .virtues {
    position: absolute; left: 0; right: 0; bottom: 0; height: 98px;
    display: flex; align-items: center; justify-content: center; gap: 22px;
    font-size: 21px; font-weight: 700; color: var(--black); padding-top: 18px;
  }
  .virtues .dot { width: 8px; height: 8px; background: var(--black); border-radius: 50%; }

  /* front side */
  .url { position: absolute; right: 26px; top: 5px; color: var(--white); font-size: 13px; }
  .title { position: absolute; left: 0; right: 0; top: 46px; text-align: center; color: var(--orange); font-weight: 700; font-size: 27px; letter-spacing: 1px; }
  .crown { position: absolute; left: 50px; top: 100px; }
  .crown-cols { display: flex; gap: 38px; margin-top: 6px; }
  .crown-col { display: flex; gap: 10px; }
  .crown-label { color: var(--orange); font-weight: 700; font-size: 15px; padding-top: 2px; }
  .crown-col .bullets li { font-size: 16px; line-height: 1.45; }
  .poem { position: absolute; left: 50px; top: 258px; width: 620px; }
  .poem .heading { font-size: 18px; line-height: 1.35; margin-bottom: 8px; }
  .poem .bullets li { line-height: 1.45; }
  .poem-author { position: absolute; left: 560px; top: 398px; font-size: 14px; font-style: italic; }
  .quote { position: absolute; left: 44px; bottom: 12px; color: var(--white); font-size: 17px; }
  .quote cite { font-style: normal; font-size: 13px; margin-left: 18px; }
</style>
</head>
<body>

<section class="card card--back" aria-label="Card back: creed and pledge">
  <svg class="frame" width="900" height="514" viewBox="0 0 900 514" aria-hidden="true">
    <path d="M0 430 Q450 402 900 430 L900 514 L0 514 Z" fill="var(--orange)"/>
  </svg>
  <div class="creed">
    <h2 class="heading">A 5-Point Creed</h2>
    <ul class="bullets">
      <li>Be intentional to grow and learn new things each day.</li>
      <li>Honour others in everything you say and do.</li>
      <li>Act with integrity and uprightness in all matters.</li>
      <li>Prioritize serving and giving to others above yourself.</li>
      <li>Dream, pray, and expect for the impossible.</li>
    </ul>
  </div>
  <div class="pledge">
    <h2 class="heading">Triple Crown &amp; 5-Point Creed Pledge:</h2>
    <p>I commit to doing my best to live out the Triple Crown and 5-Point Creed each day.</p>
    <div class="sign-line">Signature</div>
    <div class="sign-line">Date</div>
  </div>
  <div class="live-title">Live every day with:</div>
  <div class="virtues">
    <span>Passion</span><span class="dot"></span>
    <span>Wonder</span><span class="dot"></span>
    <span>Playfulness</span><span class="dot"></span>
    <span>Gratitude</span><span class="dot"></span>
    <span>Love</span>
  </div>
</section>

<section class="card card--front" aria-label="Card front: wisdom for life">
  <svg class="frame" width="900" height="514" viewBox="0 0 900 514" aria-hidden="true">
    <rect x="0" y="0" width="900" height="26" fill="var(--black)"/>
    <path d="M0 0 L150 0 L150 26 L70 26 L40 70 L0 70 Z" fill="var(--black)"/>
    <path d="M0 0 L120 0 L120 14 L60 14 L28 56 L0 56 Z" fill="var(--orange)"/>
    <rect x="0" y="470" width="900" height="44" fill="var(--black)"/>
    <path d="M900 420 L860 420 L830 470 L760 470 L760 514 L900 514 Z" fill="var(--black)"/>
    <path d="M900 436 L872 436 L844 482 L790 482 L790 514 L900 514 Z" fill="var(--orange)"/>
  </svg>
  <span class="url">www.pastthebrightline.net</span>
  <h1 class="title">WISDOM FOR LIFE</h1>
  <div class="crown">
    <h2 class="heading">The Triple Crown of Success</h2>
    <div class="crown-cols">
      <div class="crown-col"><span class="crown-label">NEVER</span>
        <ul class="bullets"><li>Lie</li><li>Cheat</li><li>Steal</li></ul></div>
      <div class="crown-col"><span class="crown-label">DON'T</span>
        <ul class="bullets"><li>Blame</li><li>Complain</li><li>Give Up</li></ul></div>
      <div class="crown-col"><span class="crown-label">ALWAYS</span>
        <ul class="bullets"><li>Be Grateful</li><li>Uplift Others</li><li>Do More Than Your Share</li></ul></div>
    </div>
  </div>
  <div class="poem">
    <h2 class="heading">Four things a man must learn to do<br>If he would make his life more true:</h2>
    <ul class="bullets">
      <li>To think without confusion clearly,</li>
      <li>To love his fellow man sincerely,</li>
      <li>To act from honest motives purely,</li>
      <li>To trust in God and Heaven securely.</li>
    </ul>
  </div>
  <span class="poem-author">Harold Vance</span>
  <p class="quote">“Make each day your masterpiece.” <cite>– Coach Walter Greer</cite></p>
</section>

</body>
</html>
```